依頼詳細
【コンテンツ】
基本的なコンテンツは、現在のページ https://korvane.jp/ を元に構成してください。
・[制作実績] ですが、[制作実績 - ホームページ] と [制作実績 - システム開発] に分けて頂き、それぞれ簡単な説明テキスト「○○○…」とイメージ画像などがあると良いかもしれません(ブロック内の正方形のサンプル画像はそのままご使用頂いても [No Photo] 等で代替して頂いても結構です)。
・[お知らせ] と [お問い合わせはこちら] の間に [よくあるご質問] のブロックを追加してください(テキストは「○○○…」で結構です)。
・その他、企業サイトによくあるようなコンテンツで おすすめのコンテンツがございましたら デザイン内にてご提案頂けますと幸いです。

【レイアウト】
・レイアウトは(現状2カラムになってますが)1カラムで構成して頂いても結構です。おすすめのレイアウトでお願いいたします(バナー広告は不要です)。
・幅は1366pxでお願いいたします(最近見かけます画面一杯に広がっているレイアウトはあまり好みではありません。背景画像が画面一杯に広がっているのは構いませんが、コンテンツは中央よりに配置したいと思います。後ほど弊社にてレスポンシブにコーディングする予定です)。
・グローバルメニューは現状の6メニューでお願いいたします。フッターメニューは常時差し替えが発生しますので「○○○」などで代替して頂いて結構です。

【配色・デザイン等】
・配色としては モノトーン(黒)を基調として頂き、見出し背景色などもモノトーンでも結構ですし、あえて一色挙げるとしますと #405080 (HSV 225度 - 50% -50%) などのネイビーまたは青などのクールな色味が好みです。その他のアイキャッチ画像やコンテンツ等の色味は単色でもカラフルなものでも結構です。ブリッカー様のセンスにお任せしたいと思います。
・ロゴマークは先日 Brikka で依頼したものですので、変更せずにそのままご使用ください。
・アイキャッチ等の写真画像は、弊社で Pelmora Images をライセンス契約しておりますので、Pelmora Images のサンプル画像をご使用頂き、別途 画像のURLを当選後にお知らせ頂けましたら結構です。
・アイキャッチ画像のイメージ(内容)ですが、弊社のサービスは 主軸サービス(バックエンド)として (1)システム開発 があり、集客用サービス(フロントエンド)として (2)ホームページ制作 があります。これらのサービスを総合すると (1) を構成する お客様の「笑顔」と弊社の「誠実さ」との「信頼関係」(人間性)がベースとなり、その上に (2) のホームページ制作(デジタルITサービス)が存在する…といったイメージになると思います。それら2つを、例えば半透明にして手前と奥で重ね合わせる/上下にレイアウトする/2枚の画像を JavaScript でアニメーション化するなどは、ブリッカー様のセンスにてお願いできましたらと思います(弊社にてコーディングしますのでご提案ください)。
サイトURL
https://korvane.jp/
ページ数
1ページ
希望イメージ
シンプル 複雑
単色 カラフル
暗い 明るい
日常 高級
遊び心 厳粛
未来的 伝統的
女性的 男性的
希望する色
青系、水色系、グレー系
納品ファイル
• フォトショップ形式 (.psd)
補足説明
Adobe Photoshop CC *psd 形式で、レイヤーを分けて制作・納品頂けますと幸いです。
予想していたよりも提案件数が少なかったので、少し内容をシンプルにして 期間を延長させて頂きました。変更箇所とその他印象等は 以下の通りでございますので、何卒よろしくお願い申し上げます。

【依頼詳細の変更】
・アイキャッチ画像のイメージ(内容)ですが「パソコンで仕事をしている人の笑顔」が含まれている画像でしたらどんなものでも結構です。(すでにご提案頂いているものにつきましては修正して頂かなくても結構です)
・「How to enjoy creative work?」というテキストは入れて頂かない方が良いかと思います(そこまで重要視しておりませんので)。
・見出しテキスト(「制作実績」「お知らせ」など)は左寄せの方が好みです。
・全体の配色ですが、カラフルな感じより 白を基調としたモノトーンな感じの方が好みです。
・[お問い合わせはこちら] ですが、今後 他のページ(ランディングページ)などにも挿入していく可能性がありますので、バナーっぽく制作頂けますと有り難いです。

白を基調としたシンプルなレイアウトで、ディテールまで洗練されていたデザインでしたので 一目見て気に入って選ばせて頂きました。
テンプレートでのデザインが主流になりつつある中、テンプレートでは表現できないような個性のあるものになったのではないかと思いまして 大変満足しております。ありがとうございました。

皆様に個別に御礼メッセージをお送りすることはできませんでしたが、予想以上の大変多くのご提案をご応募頂けまして大変満足しております。本当にありがとうございました。また機会がございましたら 何卒よろしくお願い申し上げます。

```html
<!DOCTYPE html>
<html lang="ja">
<head>
<meta charset="utf-8">
<title>Korvane Design</title>
<link rel="stylesheet" href="https://fonts.googleapis.com/css2?family=Noto+Sans+JP:wght@300;400;500;700&family=Josefin+Sans:wght@300;400&display=swap">
<style>
:root{
  --ink:#222;
  --text:#555;
  --muted:#888;
  --line:#d6d6d6;
  --paper:#fff;
  --mist:#ececee;
  --fog:#dcdcdf;
  --night:#0b0b0b;
  --navy:#405080;
}
*{margin:0;padding:0;box-sizing:border-box}
html,body{width:1200px;height:3396px;overflow:hidden}
body{font-family:"Noto Sans JP",sans-serif;color:var(--text);background:var(--paper);position:relative}
.page{position:relative;width:1200px;height:3396px;overflow:hidden}
.abs{position:absolute}

/* top */
.top-bg{left:0;top:0;width:1200px;height:1060px;background:var(--mist)}
.top-band{left:0;top:0;width:1200px;height:1060px}
.header{left:0;top:0;width:1200px;height:120px}
.nav{top:60px;display:flex;gap:34px;font-size:13px;color:var(--ink)}
.nav-left{left:140px}
.nav-right{right:150px}
.brand{left:520px;top:30px;width:160px;text-align:center;color:var(--ink)}
.brand-mark{display:block;width:26px;height:26px;margin:0 auto 6px;border:2px solid var(--ink);border-radius:50%}
.brand-name{font-family:"Josefin Sans",sans-serif;font-size:17px;letter-spacing:1px}

.mission{left:140px;top:160px;font-size:26px;font-weight:700;color:var(--ink);letter-spacing:1px}
.hero-photo{left:140px;top:228px;width:660px;height:452px;background:linear-gradient(135deg,#f3f3f3 0%,#cfd3d8 55%,#9aa0a8 100%);box-shadow:0 6px 18px rgba(0,0,0,.18)}
.side-photo{left:760px;top:340px;width:300px;height:260px;background:linear-gradient(160deg,#c7c9cd,#7d8189)}
.hero-copy{left:790px;top:452px;width:380px;height:236px;background:rgba(60,60,64,.82);color:#fff;font-size:15px;line-height:1.9;padding:34px 30px}
.intro{left:200px;top:712px;width:800px;text-align:center;font-size:13px;line-height:2.1;color:var(--text)}

/* headings */
.heading-en{font-family:"Josefin Sans",sans-serif;font-weight:300;font-size:44px;color:var(--ink);line-height:1;position:relative;display:inline-block;padding:0 4px}
.heading-en::after{content:"";position:absolute;left:0;right:0;bottom:2px;height:14px;background:var(--ink);z-index:-1}
.heading-en.dark{color:#fff}
.heading-ja{font-size:14px;font-weight:700;color:var(--ink);margin-top:10px}
.heading{z-index:1}
.service-head{left:0;top:1080px;width:1200px;text-align:center}

.service-visual{left:140px;top:1192px;width:920px;height:360px;background:linear-gradient(90deg,#7a7a7a,#b5b5b5 50%,#6c6c6c)}

.col{top:1612px;width:440px}
.col-sys{left:140px}
.col-web{left:620px}
.col h3{font-size:16px;font-weight:700;color:var(--ink);padding-bottom:14px;border-bottom:1px solid var(--line)}
.col p{font-size:12px;line-height:2;margin-top:16px;color:var(--text)}
.more{display:block;margin-top:22px;border:1px solid #aaa;height:48px;line-height:46px;text-align:center;font-size:12px;color:var(--ink)}

/* works */
.works-head{left:140px;top:1900px}
.tabs{left:140px;top:2030px;font-family:"Josefin Sans",sans-serif;font-size:24px;font-weight:300;color:var(--ink)}
.tab{display:block;width:180px;padding:6px 0 6px 0;margin-bottom:10px}
.tab.on{background:linear-gradient(90deg,var(--fog) 0,var(--fog) 60%,transparent 60%)}
.card{top:2028px;width:260px;height:284px;background:var(--paper);box-shadow:0 2px 10px rgba(0,0,0,.18)}
.card-img{position:absolute;left:0;top:0;width:260px;height:210px;background:linear-gradient(180deg,#f4f6f8,#c9d1db)}
.card-cap{position:absolute;left:20px;top:222px;font-size:13px;font-weight:500;line-height:1.6;color:var(--ink)}
.arrow{top:2138px;width:44px;height:44px;background:var(--night)}

/* news faq */
.news-head{left:140px;top:2370px}
.faq-head{left:620px;top:2370px}
.news{left:140px;top:2478px;width:440px;list-style:none}
.news li{display:flex;gap:24px;padding:14px 0;border-bottom:1px solid var(--line);font-size:12px;line-height:1.8}
.news time{color:var(--ink);font-weight:500;white-space:nowrap}
.faq{left:620px;top:2478px;width:440px;list-style:none}
.faq li{display:flex;align-items:center;gap:16px;height:52px;border-bottom:1px solid var(--line);font-size:12px}
.q{width:24px;height:20px;background:var(--navy);color:#fff;font-size:11px;text-align:center;line-height:20px;flex:none}

/* contact */
.contact{left:140px;top:2712px;width:920px;height:168px;background:linear-gradient(90deg,#3a3a3c,#6b6d72 60%,#4a4b4f)}
.contact-body{left:180px;top:2730px;width:520px;color:#fff}
.contact-body .heading-en::after{background:#888}
.contact-title{font-size:13px;font-weight:500;margin:12px 0 8px}
.contact-text{font-size:12px;line-height:1.8}

/* footer */
.footer{left:0;top:2980px;width:1200px;height:416px;background:var(--night);color:#ddd}
.footer .brand{top:40px;color:#fff}
.footer .brand-mark{border-color:#fff}
.address{left:0;top:150px;width:1200px;text-align:center;font-size:12px}
.foot-nav{left:0;top:222px;width:1200px;display:flex;justify-content:center;gap:50px;font-size:12px}
.foot-line{left:140px;top:300px;width:920px;height:1px;background:#444}
.copy{left:0;top:348px;width:1200px;text-align:center;font-size:10px;color:#999}
</style>
</head>
<body>
<div class="page">
  <div class="abs top-bg"></div>
  <svg class="abs top-band" width="1200" height="1060" aria-hidden="true">
    <polygon points="0,560 1200,120 1200,430 0,900" fill="#f7f7f8"/>
    <polygon points="0,1060 1200,760 1200,1060" fill="#fff"/>
  </svg>

  <header class="abs header">
    <nav class="abs nav nav-left"><span>ホーム</span><span>ホームページ制作</span><span>システム開発</span></nav>
    <div class="abs brand"><span class="brand-mark"></span><span class="brand-name">Korvane Design</span></div>
    <nav class="abs nav nav-right"><span>料金表</span><span>会社概要</span><span>お問い合わせ</span></nav>
  </header>

  <h1 class="abs mission">「モノ作りを楽しむ」ことをミッションとしたシステム開発デザイン会社</h1>
  <div class="abs side-photo" role="img" aria-label="オフィスで働く女性スタッフの写真"></div>
  <div class="abs hero-photo" role="img" aria-label="パソコンで仕事をする笑顔のビジネスパーソンの写真"></div>
  <p class="abs hero-copy">きめ細やかなユーザーインターフェイスと<br>シンプルなプログラム設計を軸に<br>クライアント様から「ありがとう」の一言を<br>頂戴できるよう<br>「誠実」なサービスを日々提供して参ります。</p>
  <p class="abs intro">1996年の創業から コルヴァーネデザインの創立で11年。<br>法人化して11期目の比較的若い社歴のシステム開発／ホームページ制作会社でございます。<br>自社開発で長年培った技術力と知識を活かし人間味のある社風を作り、<br>今後も10年以上先を見据えたサービスの提供をモットーとし努めて参ります。</p>

  <div class="abs heading service-head"><h2 class="heading-en">Service</h2><p class="heading-ja">サービス詳細</p></div>
  <div class="abs service-visual" role="img" aria-label="笑顔で並ぶスタッフと信頼・システム・ウェブサイトを表すモノクロのイメージ写真"></div>

  <section class="abs col col-sys">
    <h3>システム開発</h3>
    <p>業務の流れを丁寧に伺い、使う人に合わせた仕組みを設計します。受発注や顧客管理など日々の作業を効率化するシステムを、企画から運用まで一貫してお手伝いいたします。</p>
    <a class="more">システム開発について詳しく見る ›</a>
  </section>
  <section class="abs col col-web">
    <h3>ホームページ制作</h3>
    <p>集客につながる見やすく分かりやすいサイトを制作します。スマートフォン対応や更新しやすい構成など、公開後の運用まで見据えたご提案を心がけております。</p>
    <a class="more">ホームページ制作について詳しく見る ›</a>
  </section>

  <div class="abs heading works-head"><h2 class="heading-en">Works</h2><p class="heading-ja">制作事例</p></div>
  <div class="abs tabs"><span class="tab on">System</span><span class="tab">Website</span></div>
  <svg class="abs arrow" style="left:290px" width="44" height="44" aria-hidden="true"><path d="M26 14 L18 22 L26 30" stroke="#fff" stroke-width="2" fill="none"/></svg>
  <div class="abs card" style="left:334px"><div class="card-img" role="img" aria-label="サーバーのイラスト"></div><p class="card-cap">運用サーバー<br>バックアップシステム</p></div>
  <div class="abs card" style="left:614px"><div class="card-img" role="img" aria-label="サーバーのイラスト"></div><p class="card-cap">運用サーバー<br>バックアップシステム</p></div>
  <div class="abs card" style="left:894px"><div class="card-img" role="img" aria-label="サーバーのイラスト"></div><p class="card-cap">運用サーバー<br>バックアップシステム</p></div>
  <svg class="abs arrow" style="left:1134px" width="44" height="44" aria-hidden="true"><path d="M18 14 L26 22 L18 30" stroke="#fff" stroke-width="2" fill="none"/></svg>

  <div class="abs heading news-head"><h2 class="heading-en">News</h2><p class="heading-ja">お知らせ</p></div>
  <ul class="abs news">
    <li><time>2017.11.25</time><span>年末年始の営業日についてのお知らせです。<br>詳しくは本文をご確認ください。</span></li>
    <li><time>2017.11.25</time><span>ホームページ制作事例を追加いたしました。<br>ぜひ制作事例ページをご覧ください。</span></li>
    <li><time>2017.11.25</time><span>新しいサービスの提供を開始しました。<br>料金表ページに詳細を掲載しています。</span></li>
  </ul>

  <div class="abs heading faq-head"><h2 class="heading-en">FAQ</h2><p class="heading-ja">よくあるご質問</p></div>
  <ul class="abs faq">
    <li><span class="q">Q</span>制作期間はどのくらいかかりますか？</li>
    <li><span class="q">Q</span>見積もりは無料で依頼できますか？</li>
    <li><span class="q">Q</span>公開後の更新も依頼できますか？</li>
    <li><span class="q">Q</span>遠方でも相談することは可能ですか？</li>
  </ul>

  <div class="abs contact" role="img" aria-label="パソコンに向かうスタッフのモノクロ写真"></div>
  <div class="abs contact-body">
    <h2 class="heading-en dark" style="font-size:36px">Contact</h2>
    <p class="contact-title">システム・ホームページ制作のお問い合わせはこちら</p>
    <p class="contact-text">システムからウェブサイトまで、お客様のニーズに<br>合わせたご提案が可能です。お気軽にどうぞ。</p>
  </div>

  <footer class="abs footer">
    <div class="abs brand"><span class="brand-mark"></span><span class="brand-name">Korvane Design</span></div>
    <p class="abs address">〒150-0042 東京都渋谷区宇田川町8-3-12F</p>
    <nav class="abs foot-nav"><span>ホーム</span><span>ホームページ制作</span><span>システム開発</span><span>料金表</span><span>会社概要</span><span>お問い合わせ</span></nav>
    <div class="abs foot-line"></div>
    <p class="abs copy">Copyright © 1996-2017 Korvane Design INC. All Rights Reserved.</p>
  </footer>
</div>
</body>
</html>
```